SkyVelour IOS App for iPhone / Luxury private aviation / 1 main screen

Hello there !

SkyVelour Ltd is a VIP aircraft operator. You can see our https://social-example.net/skyvelour page or our https://photo-example.net/sky_velour . Our web page http://skyvelour-demo.net says it all, we don't communicate much except for the music industry activities we have.

We have developed a very simple app, 6 screens total, that will give the user a distance and a flight time between any two airports of the world. Enter a departure point (New York or JFK or KJFK...) and a destination (like Los Angeles, LAX or KLAX) and we will give you the flight time depending on the type of private jet you are selecting in the aircraft database of the app.

You might want to see the attached pdf for the flow...Any design idea is welcome.

We want it to be simple, pure, fast, and of course less will be more. We should see a unity between all these screens, same design spirit of course... On the main screen of the app, we are showing:- the company logo- a departure airport- a destination airport- the selected aircraft with access to a mini photo gallery of the said airplane- a flight time shown in hours and minutes- a distance shown in Miles, Nautical Miles or KM according to the pref page selection- an access to a contact screen- an access to a parameters screen (will develop some of it on a later version).

Thanks !!

Mathis

Target Market(s)

Private aircraft travelers and VIP flights brokers

Industry/Entity Type

Aviation

Font styles to use
Sans Serif

Colors
aaaaaa
5c5c5c
1b1b1b
e9e9e9
ffffff

Requirements
Must have
• Our logo
Nice to have
• Elegant design
Should not have
• Complicated stuff

```html
<!DOCTYPE html>
<html lang="en">
<head>
<meta charset="utf-8">
<title>SkyVelour – iOS screens</title>
<link rel="stylesheet" href="https://fonts.googleapis.com/css2?family=Inter:wght@400;500;600;700&display=swap">
<style>
  :root{
    --stage:#222326;
    --ink:#2c2e3a;
    --ink-soft:#5c5f70;
    --muted:#8d93a6;
    --sky-top:#ffffff;
    --sky-bottom:#d6e4fb;
    --card:#f3f7ff;
    --bar:#44454f;
    --bar-dark:#383943;
    --accent:#1463f3;
    --accent-dark:#0b4fd0;
    --dim:#60636f;
    --line:#c9d3e6;
    --white:#ffffff;
  }
  *{box-sizing:border-box;margin:0;padding:0}
  html,body{width:1200px;height:740px;overflow:hidden}
  body{background:var(--stage);font-family:"Inter",sans-serif;color:var(--ink);position:relative}
  .screen{position:absolute;top:103px;width:300px;height:534px;border-radius:4px;overflow:hidden;
    background:linear-gradient(180deg,var(--sky-top) 0%,var(--sky-bottom) 55%,var(--sky-bottom) 100%)}
  .screen--main{left:99px}
  .screen--search{left:450px;background:var(--dim)}
  .screen--contact{left:802px}
  .status{position:absolute;top:12px;left:27px;right:14px;display:flex;justify-content:space-between;align-items:center;font-size:11px;font-weight:600}
  .screen--search .status{color:#3d4050}
  .status-icons{display:flex;gap:4px;align-items:center}
  .brand{position:absolute;top:116px;left:0;right:0;text-align:center;font-size:22px;font-weight:400;letter-spacing:8px;color:var(--ink);padding-left:8px}
  /* main */
  .route{position:absolute;left:12px;top:176px;width:276px;height:64px;background:var(--white);box-shadow:0 2px 8px rgba(80,110,170,.12);display:flex;justify-content:space-between;align-items:center;padding:0 16px}
  .route .code{font-size:20px;font-weight:700;color:var(--ink)}
  .route .city{font-size:9.5px;letter-spacing:.4px;margin-top:4px;color:var(--ink)}
  .route .end{text-align:right}
  .route .plane{position:absolute;left:50%;top:50%;transform:translate(-50%,-50%)}
  .aircraft{position:absolute;left:12px;top:248px;width:276px;height:108px;background:linear-gradient(180deg,#e6eefc,#dbe6fb)}
  .aircraft-photo{position:absolute;left:50px;top:20px;width:176px;height:50px;border-radius:25px;background:linear-gradient(180deg,#eceef2,#b7bcc6);}
  .aircraft .arrow{position:absolute;top:52px}
  .aircraft .model{position:absolute;bottom:6px;left:0;right:0;text-align:center;font-size:9px;color:var(--muted);letter-spacing:.3px}
  .clouds{position:absolute;left:0;right:0;top:380px;height:92px;background:linear-gradient(180deg,rgba(255,255,255,0) 0%,rgba(255,255,255,.85) 70%,#fff 100%)}
  .stats{position:absolute;left:12px;right:12px;top:387px;border-top:1px solid var(--line);display:flex;height:60px}
  .stat{flex:1;padding-top:14px}
  .stat:first-child{text-align:right;padding-right:18px;border-right:1px solid var(--line)}
  .stat:last-child{padding-left:16px;position:relative}
  .stat .label{font-size:8.5px;font-weight:600;color:var(--muted);letter-spacing:.3px}
  .stat .value{font-size:20px;font-weight:600;margin-top:6px;color:var(--ink)}
  .stat .value span{font-weight:400}
  .stat .toggle{position:absolute;right:8px;top:34px}
  .tabbar{position:absolute;left:0;right:0;bottom:0;height:64px;background:linear-gradient(180deg,var(--bar),var(--bar-dark));display:flex}
  .tab{flex:1;display:flex;flex-direction:column;align-items:center;justify-content:center;gap:10px;color:#fff;font-size:10px;letter-spacing:.4px}
  .tab+.tab{border-left:1px solid #2f3038}
  /* search */
  .sheet{position:absolute;left:12px;top:36px;width:276px;height:485px;background:var(--white);overflow:hidden}
  .steps{height:64px;background:#e4ebf7;display:flex;justify-content:space-between;padding:14px 16px 0 16px;position:relative;border-bottom:1px solid var(--line)}
  .step .title{font-size:19px;font-weight:700;color:var(--ink)}
  .step .sub{font-size:9.5px;letter-spacing:.4px;margin-top:4px;color:var(--ink)}
  .step--next{text-align:right}
  .step--next .title,.step--next .sub{color:var(--ink-soft)}
  .steps .plane{position:absolute;left:50%;top:24px;transform:translateX(-50%)}
  .steps .progress{position:absolute;left:0;bottom:-1px;width:138px;height:3px;background:var(--accent)}
  .search-wrap{background:#e4ebf7;padding:8px 8px;border-bottom:1px solid var(--line)}
  .search{height:32px;background:#fff;border:1px solid var(--line);display:flex;align-items:center;justify-content:space-between;padding:0 10px 0 12px;font-size:12.5px;color:var(--ink)}
  .result{padding:14px 16px;border-bottom:1px solid var(--line);position:relative;height:64px}
  .result .code{font-size:19px;font-weight:700}
  .result .city{position:absolute;right:16px;top:20px;font-size:9.5px;letter-spacing:.3px}
  .result .name{font-size:11px;color:var(--muted);margin-top:3px;letter-spacing:.2px}
  .continue{position:absolute;left:0;right:0;bottom:0;height:52px;background:linear-gradient(180deg,var(--accent),var(--accent-dark));color:#fff;font-size:13px;font-weight:600;display:flex;align-items:center;justify-content:center}
  /* contact */
  .back{position:absolute;left:12px;top:46px}
  .call{position:absolute;left:12px;top:184px;width:276px;height:48px;background:linear-gradient(180deg,var(--bar),var(--bar-dark));color:#fff;display:flex;align-items:center;padding-left:18px}
  .call .tag{font-size:8.5px;letter-spacing:.5px;margin-left:22px;margin-right:10px;color:#c7cad6}
  .call .number{font-size:16px;letter-spacing:.3px}
  .mail{position:absolute;left:12px;top:240px;width:276px;height:48px;border:1px solid var(--ink-soft);display:flex;align-items:center;padding-left:16px;font-size:16px;color:var(--ink)}
  .mail .address{margin-left:38px}
  .social{position:absolute;left:0;right:0;top:464px;display:flex;justify-content:center;gap:28px}
  .social span{width:22px;height:22px;background:#7b7f8e;border-radius:3px;display:block}
</style>
</head>
<body>

<section class="screen screen--main">
  <div class="status"><span>9:41</span>
    <span class="status-icons">
      <svg width="14" height="8"><rect x="0" y="5" width="2.5" height="3" fill="#111"/><rect x="4" y="3.5" width="2.5" height="4.5" fill="#111"/><rect x="8" y="2" width="2.5" height="6" fill="#111"/><rect x="12" y="0" width="2" height="8" fill="#111"/></svg>
      <svg width="12" height="9"><path d="M1 3.5a7 7 0 0 1 10 0M3 5.5a4 4 0 0 1 6 0M5 7.5l1 1 1-1" stroke="#111" stroke-width="1.4" fill="none"/></svg>
      <svg width="20" height="9"><rect x=".5" y=".5" width="17" height="8" rx="2" stroke="#111" fill="none"/><rect x="2" y="2" width="14" height="5" rx="1" fill="#111"/><rect x="18.5" y="3" width="1.2" height="3" fill="#111"/></svg>
    </span>
  </div>
  <div class="brand">SKYVELOUR</div>

  <div class="route">
    <div><div class="code">JFK</div><div class="city">NEW YORK</div></div>
    <svg class="plane" width="20" height="20" viewBox="0 0 24 24"><path d="M21 12.5 13 11V5.5c0-.8-.5-2-1-2s-1 1.2-1 2V11l-8 1.5v1.5l8-.5v5l-2 1.5V21l3-.8 3 .8v-1l-2-1.5v-5l8 .5z" transform="rotate(90 12 12)" fill="#aeb8cc"/></svg>
    <div class="end"><div class="code">LAX</div><div class="city">LOS ANGELES</div></div>
  </div>

  <div class="aircraft">
    <div class="aircraft-photo" role="img" aria-label="Photo of the selected private jet, side view"></div>
    <svg class="arrow" style="left:12px" width="16" height="12" viewBox="0 0 16 12"><path d="M15 6H2M6 1 1 6l5 5" stroke="#4d7fe6" stroke-width="1.3" fill="none"/></svg>
    <svg class="arrow" style="right:12px" width="16" height="12" viewBox="0 0 16 12"><path d="M1 6h13M10 1l5 5-5 5" stroke="#4d7fe6" stroke-width="1.3" fill="none"/></svg>
    <div class="model">AERONA 757</div>
  </div>

  <div class="clouds" role="img" aria-label="Soft white clouds"></div>
  <div class="stats">
    <div class="stat"><div class="label">FLIGHT TIME</div><div class="value">02:43</div></div>
    <div class="stat"><div class="label">DISTANCE</div><div class="value">800 <span>Mile</span></div>
      <svg class="toggle" width="10" height="14" viewBox="0 0 10 14"><path d="M1 5l4-4 4 4M1 9l4 4 4-4" stroke="#5c5f70" stroke-width="1.2" fill="none"/></svg>
    </div>
  </div>

  <nav class="tabbar">
    <div class="tab">
      <svg width="20" height="18" viewBox="0 0 20 18" stroke="#fff" stroke-width="1.2" fill="none"><path d="M3 1v16M10 1v16M17 1v16M1 11h4M8 5h4M15 9h4"/></svg>
      PARAMETERS</div>
    <div class="tab">
      <svg width="18" height="18" viewBox="0 0 24 24" stroke="#fff" stroke-width="1.4" fill="none"><path d="M6 2h3l2 5-2.5 1.5a11 11 0 0 0 7 7L17 13l5 2v3a2 2 0 0 1-2 2A18 18 0 0 1 4 4a2 2 0 0 1 2-2z"/></svg>
      CONTACT</div>
  </nav>
</section>

<section class="screen screen--search">
  <div class="status"><span>9:41</span>
    <span class="status-icons">
      <svg width="14" height="8"><rect x="0" y="5" width="2.5" height="3" fill="#3d4050"/><rect x="4" y="3.5" width="2.5" height="4.5" fill="#3d4050"/><rect x="8" y="2" width="2.5" height="6" fill="#3d4050"/><rect x="12" y="0" width="2" height="8" fill="#3d4050"/></svg>
      <svg width="12" height="9"><path d="M1 3.5a7 7 0 0 1 10 0M3 5.5a4 4 0 0 1 6 0M5 7.5l1 1 1-1" stroke="#3d4050" stroke-width="1.4" fill="none"/></svg>
      <svg width="20" height="9"><rect x=".5" y=".5" width="17" height="8" rx="2" stroke="#3d4050" fill="none"/><rect x="2" y="2" width="14" height="5" rx="1" fill="#3d4050"/></svg>
    </span>
  </div>
  <div class="sheet">
    <div class="steps">
      <div class="step"><div class="title">SELECT</div><div class="sub">DEPARTURE</div></div>
      <svg class="plane" width="20" height="20" viewBox="0 0 24 24"><path d="M21 12.5 13 11V5.5c0-.8-.5-2-1-2s-1 1.2-1 2V11l-8 1.5v1.5l8-.5v5l-2 1.5V21l3-.8 3 .8v-1l-2-1.5v-5l8 .5z" transform="rotate(90 12 12)" fill="#aeb8cc"/></svg>
      <div class="step step--next"><div class="title">SELECT</div><div class="sub">DESTINATION</div></div>
      <div class="progress"></div>
    </div>
    <div class="search-wrap">
      <div class="search"><span>new yo</span>
        <svg width="13" height="13" viewBox="0 0 14 14" stroke="#aab2c4" stroke-width="1.2" fill="none"><circle cx="6" cy="6" r="4.8"/><path d="M9.5 9.5 13 13"/></svg>
      </div>
    </div>
    <div class="result">
      <div class="code">JFK</div>
      <div class="city">NEW YORK</div>
      <div class="name">Metro North International Airport</div>
    </div>
    <div class="continue">Continue</div>
  </div>
</section>

<section class="screen screen--contact">
  <div class="status"><span>9:41</span>
    <span class="status-icons">
      <svg width="14" height="8"><rect x="0" y="5" width="2.5" height="3" fill="#111"/><rect x="4" y="3.5" width="2.5" height="4.5" fill="#111"/><rect x="8" y="2" width="2.5" height="6" fill="#111"/><rect x="12" y="0" width="2" height="8" fill="#111"/></svg>
      <svg width="12" height="9"><path d="M1 3.5a7 7 0 0 1 10 0M3 5.5a4 4 0 0 1 6 0M5 7.5l1 1 1-1" stroke="#111" stroke-width="1.4" fill="none"/></svg>
      <svg width="20" height="9"><rect x=".5" y=".5" width="17" height="8" rx="2" stroke="#111" fill="none"/><rect x="2" y="2" width="14" height="5" rx="1" fill="#111"/></svg>
    </span>
  </div>
  <svg class="back" width="16" height="12" viewBox="0 0 16 12"><path d="M15 6H2M6 1 1 6l5 5" stroke="#1463f3" stroke-width="1.4" fill="none"/></svg>
  <div class="brand">SKYVELOUR</div>

  <div class="call">
    <svg width="18" height="18" viewBox="0 0 24 24" stroke="#fff" stroke-width="1.4" fill="none"><path d="M6 2h3l2 5-2.5 1.5a11 11 0 0 0 7 7L17 13l5 2v3a2 2 0 0 1-2 2A18 18 0 0 1 4 4a2 2 0 0 1 2-2z"/></svg>
    <span class="tag">CALL</span><span class="number">+100 55 01 23 45</span>
  </div>
  <div class="mail">
    <svg width="18" height="14" viewBox="0 0 18 14" stroke="#2c2e3a" stroke-width="1.3" fill="none"><rect x="1" y="1" width="16" height="12" rx="1"/><path d="M1 2l8 6 8-6"/></svg>
    <span class="address">info@skyvelour-demo.net</span>
  </div>

  <div class="social" aria-label="Social links">
    <span role="img" aria-label="Social network link"></span>
    <span role="img" aria-label="Social network link"></span>
    <span role="img" aria-label="Social network link"></span>
    <span role="img" aria-label="Photo network link"></span>
  </div>
</section>

</body>
</html>
```